Leaflet to promote a new sports massage business

I am a Remedial and Sports Massage therapist and treat a range of people from professionals who spend hours working behind computers and have associated neck and back pain through poor posture to amateur sports people of varying intensity/ability - who encounter injuries along the way, or just need some good old stretching out.Remedial and sports massage helps people who have musculoskeletal injury, pain or dysfunction brought about by the stresses and strains of life. Through massage i can reduce pain, promote recovery after injury, relieve stress, and improve flexibility. All of this contributes to helping people feel better. I have just started working at a new location (address attached) and am looking to raise awareness that I am there and to promote the benefits of massage to encourage new clients(attached as a separate document). I have a business card (attached to the brief) which uses hands as the main device, I would like to include these – possibly in some sort of logo and I would like to use purple as a key colour (if colour is used). I also want to include the KVTB logo (attached) to add credibility

```html
<!DOCTYPE html>
<html lang="en">
<head>
<meta charset="utf-8">
<title>Harriet Wexley – Remedial and Sports Massage</title>
<link rel="stylesheet" href="https://fonts.googleapis.com/css2?family=Didact+Gothic&family=Arimo:ital,wght@0,400;0,700;1,700&display=swap">
<style>
  :root{
    --purple:#7e3b8f;
    --purple-deep:#5f2670;
    --purple-soft:#a66bb5;
    --ink:#3f3f3f;
    --paper:#ffffff;
    --skin:#e9c3aa;
    --sky:#dfe8ee;
  }
  *{margin:0;padding:0;box-sizing:border-box}
  html,body{width:900px;height:1200px;overflow:hidden;background:var(--paper)}
  .leaflet{position:relative;width:900px;height:1200px;overflow:hidden;background:var(--paper);font-family:"Didact Gothic",sans-serif;color:var(--ink)}
  .therapist-name{position:absolute;left:44px;top:34px;font-size:86px;color:var(--purple);font-weight:400;letter-spacing:1px}
  .therapist-role{position:absolute;left:48px;top:150px;font-size:40px;color:var(--ink)}
  .email-bar{position:absolute;left:300px;top:232px;width:600px;height:50px;background:var(--purple);clip-path:polygon(28px 0,100% 0,100% 100%,0 100%);color:#fff;font-size:22px;line-height:50px;padding-left:56px}
  .hero-photo{position:absolute;left:0;top:298px;width:900px;height:412px;background:radial-gradient(circle at 30% 40%,var(--skin) 0 22%,transparent 45%),linear-gradient(120deg,#f4f7fa,var(--sky) 60%,#c9d6e0)}
  .hero-panel{position:absolute;left:0;top:298px}
  .hero-text{position:absolute;left:605px;top:330px;width:275px;color:#fff}
  .hero-title{font-family:"Arimo",sans-serif;font-weight:700;font-size:37px;line-height:1.15}
  .hero-call{margin-top:34px;font-size:24px}
  .hero-phone{font-family:"Arimo",sans-serif;font-weight:700;font-size:38px;margin-top:6px;white-space:nowrap}
  .tagline-tab{position:absolute;left:190px;top:710px;height:42px;width:200px;background:var(--purple-deep);color:#fff;font-family:"Arimo",sans-serif;font-weight:700;font-style:italic;font-size:22px;line-height:42px;text-align:center;clip-path:polygon(0 0,100% 0,92% 100%,8% 100%)}
  .about{position:absolute;left:40px;top:775px;width:370px;font-size:17px;line-height:1.4;text-align:justify}
  .benefits{position:absolute;left:470px;top:770px;width:410px}
  .benefits-title{font-size:34px;color:var(--purple);font-weight:400}
  .benefits-list{list-style:none;margin-top:8px}
  .benefits-list li{font-size:24px;line-height:1.4;padding-left:30px;position:relative}
  .benefits-list li::before{content:"";position:absolute;left:0;top:11px;width:16px;height:16px;background:var(--purple)}
  .social-line{position:absolute;left:470px;top:1022px;font-size:19px;color:var(--ink);display:flex;align-items:center;gap:10px}
  .social-dot{width:24px;height:24px;border-radius:50%;background:var(--purple)}
  .hands-art{position:absolute;left:0;top:1000px;width:250px;height:200px;background:linear-gradient(135deg,var(--purple-soft),var(--purple-deep));clip-path:polygon(0 20%,60% 0,100% 55%,100% 100%,0 100%)}
  .address{position:absolute;left:262px;top:1082px;width:480px;color:var(--purple)}
  .address-label{font-size:26px;white-space:nowrap}
  .address-street{font-family:"Arimo",sans-serif;font-weight:700;font-size:23px;margin-top:4px;white-space:nowrap}
  .partner-mark{position:absolute;left:760px;top:1062px;width:120px;display:flex;flex-direction:column;align-items:center;gap:6px}
  .partner-circle{width:72px;height:72px;border-radius:50%;border:4px solid var(--purple)}
  .partner-name{font-size:22px;color:var(--purple)}
</style>
</head>
<body>
<main class="leaflet">
  <h1 class="therapist-name">Harriet Wexley</h1>
  <p class="therapist-role">Remedial and sports Massage therapist</p>
  <div class="email-bar">email: harrietwexley@mailbox.example</div>

  <div class="hero-photo" role="img" aria-label="Photo of a woman from behind holding her sore neck and shoulder"></div>
  <svg class="hero-panel" width="900" height="412" viewBox="0 0 900 412">
    <polygon points="640,0 900,0 900,412 560,412 590,40" fill="var(--purple)" opacity="0.95"/>
  </svg>
  <div class="hero-text">
    <div class="hero-title">Remedial and Sports Massage Therapist</div>
    <div class="hero-call">Call to Harriet Wexley:</div>
    <div class="hero-phone">07700 900412</div>
  </div>

  <div class="tagline-tab">Will Be GOOD!!!</div>

  <p class="about">I am a Remedial and Sports Massage therapist and treat a range of people from professionals who spend hours working behind computers and have associated neck and back pain through poor posture to amateur sports people of varying intensity / ability – who encounter injuries along the way, or just need some good old stretching out.</p>

  <section class="benefits">
    <h2 class="benefits-title">Benefits of Massage</h2>
    <ul class="benefits-list">
      <li>Reduces pain</li>
      <li>Promotes recovery</li>
      <li>Improves posture and flexibility</li>
      <li>Relieves stress</li>
      <li>Improves health and wellbeing</li>
    </ul>
  </section>

  <div class="social-line">wexleymassage.example/page <span class="social-dot"></span></div>

  <div class="hands-art" role="img" aria-label="Illustration of two hands, the business's visual device"></div>

  <div class="address">
    <div class="address-label">New Address: Ashcombe Athletic Ground</div>
    <div class="address-street">Millbrook Road, Ashcombe, AB1 2CD</div>
  </div>

  <div class="partner-mark">
    <span class="partner-circle"></span>
    <span class="partner-name">KVTB</span>
  </div>
</main>
</body>
</html>
```